I own a company on Maui, called Coral Haven and we are hosting our first LGBT Golf Tournament on Tuesday, June 9, 2015, titled The Rainbow Open 2015 and need a poster design enticing and inviting golf players to participate by playing in our 1st LGBT Golf Tournament, etc.
Updates

Aloha~ Since this poster is for a LGBT Golf Tournament, I will provide more detailed information as we go along. For example, times, dates, prizes, charity organization, etc. You may review both www.coralhaventours.example, the Host of the tournament and www.therainbowopen.example. the actual site for the tournament. If you have any questions, please contact me. Mahalo!

Industry/Entity Type

It Company

```html
<!DOCTYPE html>
<html lang="en">
<head>
<meta charset="utf-8">
<title>The Rainbow Open 2015 – Coral Haven</title>
<link rel="stylesheet" href="https://fonts.googleapis.com/css2?family=Antic+Didone&family=Anton&family=Arimo&display=swap">
<style>
  :root {
    --backdrop: #2a2a2a;
    --sheet-top: #3bb3a3;
    --sheet-mid: #8fdf7c;
    --sheet-bottom: #2b9db2;
    --date-ink: #dcfbf5;
    --date-shadow: #1d5a52;
    --title-ink: #111511;
    --ball-ink: #2f6a12;
    --rule: #1d6f8a;
    --body-ink: #0d1a1c;
  }
  * { margin: 0; padding: 0; box-sizing: border-box; }
  html, body {
    width: 879px; height: 1200px; overflow: hidden;
    background: var(--backdrop);
  }
  .poster {
    position: absolute; left: 55px; top: 60px;
    width: 770px; height: 1080px; overflow: hidden;
    background:
      radial-gradient(ellipse 60% 45% at 55% 40%, var(--sheet-mid) 0%, rgba(143,223,124,0) 100%),
      linear-gradient(180deg, var(--sheet-top) 0%, #6fd08a 35%, #5cc49a 62%, var(--sheet-bottom) 100%);
  }
  .event-date {
    position: absolute; left: 0; top: 22px; width: 100%;
    text-align: center;
    font-family: "Antic Didone", serif;
    font-weight: 400;
    font-size: 84px; line-height: 1;
    color: var(--date-ink);
    text-shadow: 2px 3px 0 var(--date-shadow);
    white-space: nowrap;
    transform: scale(0.8, 1.15);
  }
  .hero-art {
    position: absolute; left: 60px; top: 130px;
    width: 650px; height: 550px;
  }
  .ball-caption {
    position: absolute; left: 235px; top: 372px;
    width: 360px;
    font-family: "Antic Didone", serif;
    font-weight: 400;
    font-size: 42px; line-height: 46px;
    color: var(--ball-ink);
    text-align: center;
    white-space: nowrap;
    transform: rotate(20deg);
  }
  .event-title {
    position: absolute; left: 140px; top: 545px;
    width: 410px; height: 265px;
    font-family: "Anton", sans-serif;
    font-weight: 400;
    text-transform: uppercase;
  }
  .event-title svg { display: block; width: 100%; height: 100%; overflow: visible; }
  .event-title text { fill: var(--title-ink); font-family: "Anton", sans-serif; }
  .event-year {
    position: absolute; left: 555px; top: 555px;
    width: 250px; height: 110px;
    font-family: "Antic Didone", serif;
    font-weight: 400;
    font-size: 118px; line-height: 110px;
    color: var(--title-ink);
    white-space: nowrap;
    transform-origin: 0 0;
    transform: translate(110px, 0) rotate(90deg);
    letter-spacing: 6px;
  }
  .rule {
    position: absolute; left: 35px; width: 700px; height: 4px;
    background: var(--rule); border-radius: 2px;
  }
  .rule-top { top: 826px; }
  .rule-bottom { top: 941px; }
  .details {
    position: absolute; left: 0; width: 100%;
    font-family: "Arimo", sans-serif;
    font-size: 15px; line-height: 21px;
    color: var(--body-ink);
    text-align: center;
  }
  .details-main { top: 845px; }
  .details-extra { top: 960px; left: 190px; width: 390px; }
</style>
</head>
<body>
  <main class="poster">
    <h2 class="event-date">June 9, 2015</h2>

    <svg class="hero-art" viewBox="0 0 650 550" role="img"
         aria-label="Illustration of a large golf ball on a green ring with golfer silhouettes, a golf cart, checkered flags and paint splatters">
      <defs>
        <radialGradient id="ballShade" cx="45%" cy="40%" r="60%">
          <stop offset="0" stop-color="#ffffff"/>
          <stop offset="0.7" stop-color="#e6ebe6"/>
          <stop offset="1" stop-color="#b9c4bb"/>
        </radialGradient>
        <radialGradient id="haloShade" cx="50%" cy="50%" r="50%">
          <stop offset="0" stop-color="#6fb53a" stop-opacity="0.55"/>
          <stop offset="1" stop-color="#6fb53a" stop-opacity="0"/>
        </radialGradient>
      </defs>
      <ellipse cx="345" cy="290" rx="320" ry="260" fill="url(#haloShade)"/>
      <circle cx="350" cy="340" r="180" fill="#4f8f1c"/>
      <circle cx="350" cy="340" r="168" fill="url(#ballShade)"/>
    </svg>

    <p class="ball-caption">1st LGBT<br>Golf Tournament</p>

    <h1 class="event-title" aria-label="The Rainbow Open">
      <svg viewBox="0 0 410 265" aria-hidden="true">
        <text x="8" y="110" font-size="140" textLength="395" lengthAdjust="spacingAndGlyphs">THE RAINBOW</text>
        <text x="4" y="258" font-size="186" textLength="396" lengthAdjust="spacingAndGlyphs">OPEN</text>
      </svg>
    </h1>
    <div class="event-year">2015</div>

    <div class="rule rule-top"></div>
    <p class="details details-main">
      Lorem ipsum dolor sit amet, consectetuer adipiscing elit, sed diam nonummy nibh<br>
      euismod tincidunt ut laoreet dolore magna aliquam erat volutpat.<br>
      Ut wisi enim ad minim veniam, quis nostrud exerci tation ullamcorper suscipit lobortis<br>
      nisl ut aliquip ex ea commodo consequat.
    </p>
    <div class="rule rule-bottom"></div>
    <p class="details details-extra">
      Lorem ipsum dolor sit amet, consectetuer<br>
      adipiscing elit, sed diam nonummy nibh euis-<br>
      mod tincidunt ut laoreet dolore magna ali-<br>
      quam erat volutpat.
    </p>
  </main>
</body>
</html>
```